Commercial and Residential Paint Contractor needs website

We need a website for our residential painting, multi-family painting and commercial painting company. We paint interior and exterior of houses, apartments and commercial buildings. I would like an about us page, residential page, multi family page, commercial page and contact us. Need keywords added to website for seo opitimazation. I like this website https://www.velmorandhalestudio.com/

Target Market(s)

General Contractors and commercial property managers

Coding

Coded - Design and coding required

Number of Pages Required

5+ page

Font styles to use
Sans Serif

Requirements
Must have
• I need SEO keywords on pages

```html
<!DOCTYPE html>
<html lang="en">
<head>
<meta charset="utf-8">
<title>Halden Coatings – Residential, Multi Family &amp; Commercial Painting</title>
<meta name="description" content="Residential painting, multi-family painting and commercial painting contractor. Interior and exterior painting for houses, apartments and commercial buildings.">
<link href="https://fonts.googleapis.com/css2?family=Roboto:wght@300;400;500;700&amp;family=Kaushan+Script&amp;family=Michroma&amp;display=swap" rel="stylesheet">
<style>
:root{
  --navy:#1c4d8c;
  --blue:#1d5aa0;
  --deep-blue:#124a98;
  --peach:#f2c488;
  --red:#c9253a;
  --bright-red:#e3222c;
  --cyan:#4fe0f0;
  --green:#1fa88a;
  --ink:#2b5a93;
  --grey:#777;
  --black:#000;
  --white:#fff;
}
*{box-sizing:border-box;margin:0;padding:0}
html,body{width:1200px;height:3147px;overflow:hidden}
body{position:relative;font-family:'Roboto',sans-serif;background:var(--white);color:#333}
.abs{position:absolute}

/* header */
.site-header{position:absolute;left:0;top:0;width:1200px;height:80px;background:var(--white)}
.brand{position:absolute;left:114px;top:24px;display:flex;align-items:center;gap:10px;font:700 26px 'Roboto',sans-serif;color:var(--navy);letter-spacing:1px}
.brand-mark{width:22px;height:22px;background:var(--navy)}
.main-nav a{position:absolute;top:32px;height:28px;line-height:28px;font:500 12.5px 'Roboto',sans-serif;letter-spacing:2.2px;color:var(--navy);text-decoration:none}
.main-nav a.active{background:var(--navy);color:var(--white);padding:0 13px;font-weight:700}
.rainbow{position:absolute;left:0;width:1200px;background:linear-gradient(90deg,#d8202a,#f08a1c,#f6d21c,#8cc63e,#2cae9a,#2a6fc0,#6a3fa8,#c8368a,#d9c9a0,#e8e0d0)}

/* hero */
.hero{position:absolute;left:0;top:86px;width:1200px;height:504px}
.hero-photo{position:absolute;inset:0;background:linear-gradient(180deg,#3a3c40 0%,#2a2d33 40%,#1d2027 70%,#4a4640 100%)}
.hero-title{position:absolute;left:111px;color:var(--cyan);font:400 32px 'Roboto',sans-serif;letter-spacing:2px}
.hero-title .script{font-family:'Kaushan Script',cursive;color:var(--white);font-size:50px;letter-spacing:0}
.hero-rule{position:absolute;left:111px;top:194px;width:84px;height:5px;background:var(--cyan)}
.hero-text{position:absolute;left:113px;top:218px;width:340px;color:var(--white);font:500 12.5px/19px 'Roboto',sans-serif}
.btn-solid{position:absolute;left:111px;top:309px;width:226px;height:50px;background:var(--red);color:var(--white);font:400 21px/50px 'Roboto',sans-serif;text-align:center;letter-spacing:1px}

.signup-card{position:absolute;left:777px;top:144px;width:307px;height:390px;background:rgba(255,255,255,.96);text-align:center}
.signup-card h2{margin-top:22px;font:400 23px 'Roboto',sans-serif;color:#555}
.signup-card .sub{margin-top:10px;font:300 11px 'Roboto',sans-serif;color:#888}
.field{position:absolute;left:23px;width:260px;height:30px;border-bottom:1px solid #ddd;text-align:left;font:400 11px/30px 'Roboto',sans-serif;color:#777;padding-left:34px}
.field svg{position:absolute;left:6px;top:9px}
.signup-btn{position:absolute;left:23px;top:285px;width:260px;height:32px;background:var(--green);color:var(--white);font:700 13px/32px 'Roboto',sans-serif}
.terms{position:absolute;left:30px;top:334px;width:247px;font:300 9px/13px 'Roboto',sans-serif;color:#888}
.terms span{color:var(--green)}

/* services */
.services{position:absolute;left:0;top:590px;width:1200px;height:720px;background:linear-gradient(180deg,#1a4f92 0%,var(--blue) 20%,#1f5ca3 100%)}
.section-title{position:absolute;left:0;width:1200px;text-align:center;font:400 31px 'Roboto',sans-serif;letter-spacing:2.5px}
.section-sub{position:absolute;left:0;width:1200px;text-align:center;font:400 14px 'Roboto',sans-serif;letter-spacing:2.8px}
.service-card{position:absolute;top:237px;width:277px;height:386px}
.service-photo{position:absolute;inset:0}
.ribbon{position:absolute;right:-9px;top:-9px}
.service-label{position:absolute;left:24px;top:358px;width:232px;height:56px;border-radius:28px 10px 28px 10px;color:var(--white);font:500 20px/56px 'Roboto',sans-serif;text-align:center;letter-spacing:1px}

/* features */
.features{position:absolute;left:0;top:1310px;width:1200px;height:700px;background:var(--white)}
.divider-v{position:absolute;top:147px;height:391px;border-left:1.5px dashed #2e5d9a}
.divider-h{position:absolute;left:172px;top:352px;width:854px;border-top:1.5px dashed #2e5d9a}
.feature{position:absolute;width:260px;text-align:center;font:400 16px 'Roboto',sans-serif;color:var(--ink);letter-spacing:.8px}
.feature svg{display:block;margin:0 auto 16px}
.btn-outline{position:absolute;left:445px;width:308px;height:58px;border:1.5px solid var(--red);color:var(--red);font:400 20px/56px 'Roboto',sans-serif;text-align:center;letter-spacing:1.5px;background:var(--white)}

/* gallery */
.gallery{position:absolute;left:0;top:2010px;width:1200px;height:770px;background:radial-gradient(ellipse at 15% 45%,#2a5fb0 0%,var(--deep-blue) 40%,#0f3f88 100%)}
.frame{position:absolute;background:var(--black)}
.frame .shot{position:absolute}

/* footer */
.site-footer{position:absolute;left:0;top:2795px;width:1200px;height:352px;background:var(--black);color:var(--white)}
.footer-title{position:absolute;top:30px;font:400 22px 'Michroma',sans-serif;color:var(--bright-red);letter-spacing:6px}
.footer-divider{position:absolute;top:23px;height:255px;border-left:1px solid #555}
.footer-links a{position:absolute;left:106px;font:700 12px 'Roboto',sans-serif;letter-spacing:2.4px;color:var(--white);text-decoration:none}
.contact-row{position:absolute;left:494px;display:flex;align-items:center;gap:14px;font:700 12px/24px 'Roboto',sans-serif}
.about-text{position:absolute;left:827px;top:82px;width:260px;font:400 10.5px/16px 'Roboto',sans-serif;text-align:justify}
.footer-brand{position:absolute;left:827px;top:249px;display:flex;align-items:center;gap:8px;font:700 22px 'Roboto',sans-serif;color:var(--white);letter-spacing:1px}
.footer-brand i{width:16px;height:16px;background:var(--white)}
.footer-rule{position:absolute;left:106px;top:311px;width:974px;border-top:1px solid #888}
.copyright{position:absolute;left:106px;top:326px;font:400 8px 'Roboto',sans-serif}
</style>
</head>
<body>

<header class="site-header">
  <div class="brand"><span class="brand-mark"></span>HALDEN COATINGS</div>
  <nav class="main-nav">
    <a class="active" style="left:461px" href="#">Home</a>
    <a style="left:555px" href="#">Residential</a>
    <a style="left:677px" href="#">Multi Family</a>
    <a style="left:802px" href="#">Commercial</a>
    <a style="left:926px" href="#">About Us</a>
    <a style="left:1024px" href="#">Contact</a>
  </nav>
</header>
<div class="rainbow" style="top:80px;height:6px"></div>

<section class="hero">
  <div class="hero-photo" role="img" aria-label="Freshly painted gym interior with a large patterned feature wall"></div>
  <h1 class="hero-title" style="top:50px"><span class="script">Painting</span> House Is</h1>
  <div class="hero-title" style="top:108px">Our <span class="script">Passion!</span></div>
  <div class="hero-rule"></div>
  <p class="hero-text">Lorem Ipsum is simply dummy text of the printing and typesetting industry. Lorem Ipsum has been the indus try's standard dummy text ever since the 1500</p>
  <div class="btn-solid">Get A Quote</div>

  <form class="signup-card" style="top:58px">
    <h2>Create Account</h2>
    <p class="sub">It's free and hardly takes more than 30 seconds.</p>
    <div class="field" style="top:100px"><svg width="12" height="13" viewBox="0 0 12 13"><circle cx="6" cy="3.5" r="3" fill="#555"/><path d="M0 13c0-4 2.5-6 6-6s6 2 6 6z" fill="#555"/></svg>Username</div>
    <div class="field" style="top:146px"><svg width="13" height="12" viewBox="0 0 13 12"><path d="M13 0L0 5l5 2 1 5 2-4z" fill="#555"/></svg>Email Address</div>
    <div class="field" style="top:192px"><svg width="11" height="13" viewBox="0 0 11 13"><path d="M2.5 6V4a3 3 0 016 0v2" stroke="#555" stroke-width="1.6" fill="none"/><rect y="6" width="11" height="7" rx="1" fill="#555"/></svg>Password</div>
    <div class="field" style="top:238px"><svg width="11" height="13" viewBox="0 0 11 13"><path d="M2.5 6V4a3 3 0 016 0v2" stroke="#555" stroke-width="1.6" fill="none"/><rect y="6" width="11" height="7" rx="1" fill="#555"/></svg>Confirm Password</div>
    <div class="signup-btn">Sign Up</div>
    <p class="terms">By clicking the Sign Up button, you agree to our <span>Terms &amp; Conditions</span>, and <span>Privacy Policy</span>.</p>
  </form>
</section>

<section class="services">
  <h2 class="section-title" style="top:125px;color:var(--peach)">Why We Are The Best?</h2>
  <p class="section-sub" style="top:168px;color:var(--white)">Lorem Ipsum is simply dummy text of the printing</p>

  <article class="service-card" style="left:110px">
    <div class="service-photo" role="img" aria-label="Painters choosing colour swatches against a white wall" style="background:linear-gradient(135deg,#cfcac4,#e8e6e2 55%,#9a8f86)"></div>
    <svg class="ribbon" width="90" height="90" viewBox="0 0 90 90"><path d="M0 0h32l58 58v32z" fill="#8e5ce0"/></svg>
    <div class="service-label" style="background:linear-gradient(90deg,#3f63d8,#8a5ce4)">RESIDENTIAL</div>
  </article>
  <article class="service-card" style="left:459px">
    <div class="service-photo" role="img" aria-label="Bright office interior with a person working at a desk" style="background:linear-gradient(135deg,#f2f2f0,#dcdad6 55%,#8f8b86)"></div>
    <svg class="ribbon" width="90" height="90" viewBox="0 0 90 90"><path d="M0 0h32l58 58v32z" fill="#f3a43a"/></svg>
    <div class="service-label" style="background:linear-gradient(90deg,#e6344a,#f4a03a)">COMMERCIAL</div>
  </article>
  <article class="service-card" style="left:808px">
    <div class="service-photo" role="img" aria-label="Family painting a wall in light blue with rollers" style="background:linear-gradient(135deg,#e4e4e2,#d6d3cf 55%,#a89a86)"></div>
    <svg class="ribbon" width="90" height="90" viewBox="0 0 90 90"><path d="M0 0h32l58 58v32z" fill="#e33a6a"/></svg>
    <div class="service-label" style="background:linear-gradient(90deg,#8a3fd0,#e2367a)">MULTI &nbsp;FAMILY</div>
  </article>
</section>

<section class="features">
  <h2 class="section-title" style="top:36px;color:var(--red)">Why Choose Us?</h2>
  <p class="section-sub" style="top:80px;color:var(--grey);font-weight:300">Lorem Ipsum is simply dummy text of the printing</p>
  <div class="divider-v" style="left:420px"></div>
  <div class="divider-v" style="left:780px"></div>
  <div class="divider-h"></div>

  <div class="feature" style="left:121px;top:156px">
    <svg width="56" height="70" viewBox="0 0 56 70"><defs><linearGradient id="gRoller" x1="0" y1="0" x2="0" y2="1"><stop offset="0" stop-color="#fbc02d"/><stop offset="1" stop-color="#f26a21"/></linearGradient></defs><rect x="2" y="2" width="50" height="16" rx="3" fill="url(#gRoller)"/><path d="M52 10h3v18H28v10" stroke="#f26a21" stroke-width="3" fill="none"/><rect x="23" y="38" width="10" height="30" rx="3" fill="#e02b3a"/></svg>
    Faux Finishes</div>
  <div class="feature" style="left:470px;top:148px">
    <svg width="70" height="78" viewBox="0 0 70 78"><defs><linearGradient id="gBucket" x1="0" y1="0" x2="0" y2="1"><stop offset="0" stop-color="#2a5fd8"/><stop offset="1" stop-color="#d6307a"/></linearGradient></defs><path d="M6 30a29 29 0 0158 0" stroke="#2a5fd8" stroke-width="4" fill="none"/><ellipse cx="35" cy="30" rx="29" ry="8" fill="none" stroke="url(#gBucket)" stroke-width="4"/><path d="M6 30v38q0 8 29 8t29-8V30" fill="none" stroke="url(#gBucket)" stroke-width="4"/><path d="M14 40h42v10q-4 6-6 0-3 8-7 0-3 6-6 0-3 8-7 0-3 6-6 0-3 6-6 0-4 6-4 0z" fill="#c8307a"/></svg>
    Water Proofing</div>
  <div class="feature" style="left:811px;top:156px">
    <svg width="70" height="70" viewBox="0 0 70 70"><defs><linearGradient id="gScreen" x1="0" y1="0" x2="1" y2="1"><stop offset="0" stop-color="#c23ad8"/><stop offset="1" stop-color="#f2a020"/></linearGradient></defs><rect x="3" y="3" width="60" height="48" rx="3" fill="none" stroke="url(#gScreen)" stroke-width="5"/><rect x="10" y="10" width="46" height="34" fill="#f25aa8"/><path d="M22 22l14 12 20 28" stroke="#f2a020" stroke-width="6" fill="none"/><circle cx="24" cy="22" r="6" fill="#fff"/></svg>
    Pre-Paint Demo</div>
  <div class="feature" style="left:121px;top:426px">
    <svg width="44" height="62" viewBox="0 0 44 62"><defs><linearGradient id="gDrop" x1="0" y1="0" x2="0" y2="1"><stop offset="0" stop-color="#17c0b0"/><stop offset="1" stop-color="#5ed85a"/></linearGradient></defs><path d="M22 2C14 18 2 28 2 40a20 20 0 0040 0C42 28 30 18 22 2z" fill="url(#gDrop)"/></svg>
    Mildew Removal</div>
  <div class="feature" style="left:470px;top:422px">
    <svg width="70" height="70" viewBox="0 0 70 70"><defs><linearGradient id="gTag" x1="0" y1="0" x2="0" y2="1"><stop offset="0" stop-color="#8a2ae0"/><stop offset="1" stop-color="#f23a8a"/></linearGradient></defs><path d="M38 18l20 22-20 22z" fill="none" stroke="#d03ad8" stroke-width="3"/><rect x="10" y="2" width="28" height="68" rx="8" fill="url(#gTag)"/><circle cx="24" cy="14" r="4" fill="#fff"/></svg>
    Color Proof</div>
  <div class="feature" style="left:811px;top:422px">
    <svg width="80" height="74" viewBox="0 0 80 74"><defs><linearGradient id="gBrush" x1="0" y1="0" x2="1" y2="1"><stop offset="0" stop-color="#1fc0b0"/><stop offset="1" stop-color="#3a48d8"/></linearGradient></defs><path d="M76 2L34 50" stroke="url(#gBrush)" stroke-width="8" stroke-linecap="round"/><path d="M30 46c-8 0-14 8-12 18 10 2 18-4 18-12z" fill="#7a38d8"/><path d="M16 34c-10 6-10 24 4 30" stroke="#2a48c8" stroke-width="5" fill="none" stroke-linecap="round"/></svg>
    Window Washing</div>

  <div class="btn-outline" style="top:599px">Get A Quote</div>
</section>

<section class="gallery">
  <h2 class="section-title" style="top:30px;color:var(--peach)">Our Gallery</h2>
  <p class="section-sub" style="top:75px;color:var(--white)">Lorem Ipsum is simply dummy text of the printing</p>

  <div class="frame" style="left:170px;top:138px;width:357px;height:501px">
    <div class="shot" role="img" aria-label="Painted kitchen interior with pendant lights and a brick archway" style="left:45px;top:47px;width:265px;height:408px;background:linear-gradient(180deg,#3a3530,#8a7e70 40%,#d8d2c8 75%,#6a6258)"></div>
  </div>
  <div class="frame" style="left:617px;top:137px;width:384px;height:240px">
    <div class="shot" role="img" aria-label="Freshly painted single-storey commercial building with lawn" style="left:25px;top:22px;width:333px;height:192px;background:linear-gradient(180deg,#bcd2ee 0%,#9a8a78 45%,#7a8a5a 80%,#a8b08a 100%)"></div>
  </div>
  <div class="frame" style="left:617px;top:401px;width:384px;height:240px">
    <div class="shot" role="img" aria-label="Exterior of a painted brick office building under blue sky" style="left:25px;top:22px;width:335px;height:193px;background:linear-gradient(180deg,#5a8ed8 0%,#9cc0ea 35%,#8a7868 60%,#b0a890 100%)"></div>
  </div>

  <div class="btn-outline" style="top:678px;border-color:var(--white)">Know More</div>
</section>

<div class="rainbow" style="top:2780px;height:15px"></div>

<footer class="site-footer">
  <h3 class="footer-title" style="left:109px">TAGS</h3>
  <h3 class="footer-title" style="left:496px">ADDRESS</h3>
  <h3 class="footer-title" style="left:827px">ABOUT US</h3>
  <div class="footer-divider" style="left:424px"></div>
  <div class="footer-divider" style="left:759px"></div>

  <nav class="footer-links">
    <a style="top:84px" href="#">Home</a>
    <a style="top:121px" href="#">About</a>
    <a style="top:155px" href="#">Residential</a>
    <a style="top:193px" href="#">Multi Family</a>
    <a style="top:232px" href="#">Commercial</a>
    <a style="top:269px" href="#">Contact</a>
  </nav>

  <div class="contact-row" style="top:82px;align-items:flex-start">
    <svg width="22" height="32" viewBox="0 0 22 32"><path d="M11 0a11 11 0 00-11 11c0 8 11 21 11 21s11-13 11-21A11 11 0 0011 0z" fill="#fff"/><circle cx="11" cy="11" r="4" fill="#000"/></svg>
    <span>Lorem Ipsum is simply dummy text of<br>the printing and typesetting industry.</span>
  </div>
  <div class="contact-row" style="top:161px">
    <svg width="24" height="24" viewBox="0 0 24 24"><path d="M5 2l4 5-2 3c1 3 4 6 7 7l3-2 5 4-3 4C10 23 1 14 1 5z" fill="#fff"/></svg>
    <span>555-014-2290</span>
  </div>
  <div class="contact-row" style="top:222px">
    <svg width="30" height="20" viewBox="0 0 30 20"><rect x="1" y="1" width="28" height="18" fill="none" stroke="#fff" stroke-width="2"/><path d="M1 1l14 11L29 1M1 19l10-9M29 19l-10-9" stroke="#fff" stroke-width="2" fill="none"/></svg>
    <span>info@haldencoatings.com</span>
  </div>

  <p class="about-text">We are family owned and operated with over 10 years' experience. We pride our self in performing to the highest degree of workmanship standards. Halden Coatings is your best choice for commercial, residential and multi-family painting in the Greater Lakeview area. Our experienced estimators will meet with you and customize a proposal to meet your needs. They will stay with you from the beginning of the project to the end, making sure you are 100% satisfied.</p>
  <div class="footer-brand"><i></i>HALDEN COATINGS</div>

  <div class="footer-rule"></div>
  <p class="copyright">COPYRIGHT 2020/ Halden Coatings</p>
</footer>

</body>
</html>
```